New Flyer Design Project

We need a flyer for our upcoming Rising Builders Summit.

5th Annual Rising Builders Summit
by the Bureau for Advancement in Public Works (B-AdPW)
Theme: Stand Tall
Date: January 24, 2020
Location: Harborview Lodge Hotel and Conference Center, San Marcos, TX
#StandTall

This is event is put together by B-AdPW's Rising Builders Ring of Merit. I have a logo for the Ring of Merit, but not something that indicates it's the Rising Builders Ring.

More about the Forum (please don't include on the flyer): This Forum provides a venue to openly discuss issues affecting women in our industry and ideas and strategies to address those issues.

Architecture, Construction and Engineering are all struggling with a tremendous shortage of skilled talent. It is more important than ever for organizations to be able to attract, support and retain a talented workforce and to encourage more women to pursue and build vibrant careers in architecture, engineering and construction. Unfortunately, their attrition rate also remains high in these industries. Developing and retaining a skilled workforce includes identifying and addressing the specific needs of women in our industry. Man or Woman; Male or Female Brain, B-AdPW’s Rising Builders Summit will give you and your team the tools you need to excel as an Employer of Choice and a roadmap for individual continued career planning and success .

This unique Forum provides a venue to engage everyone from executives to those just beginning their careers with active, hands-on sessions and vibrant networking with the best and brightest in the A/E/C industry. In our usual B-AdPW Forum style, Keynotes become table participants and table participants become presenters, encouraging participants to assimilate what they are learning. Join local, state and national leaders and subject matter experts as we candidly explore and address the issues affecting women in our industry .

```html
<!DOCTYPE html>
<html lang="en">
<head>
<meta charset="utf-8">
<title>5th Annual Rising Builders Summit</title>
<link rel="stylesheet" href="https://fonts.googleapis.com/css2?family=Montserrat:wght@500;600;700;800&family=Arimo:wght@400&display=swap">
<style>
  :root {
    --brand-blue: #1f3f93;
    --brand-green: #8cb23d;
    --ink: #3a3a3a;
    --paper: #ffffff;
    --backdrop: #606060;
  }
  * { margin: 0; padding: 0; box-sizing: border-box; }
  html, body { width: 1200px; height: 2504px; overflow: hidden; }
  body { background: var(--backdrop); position: relative; }

  .flyer {
    position: absolute; left: 40px; top: 475px;
    width: 1120px; height: 1553px;
    background: var(--paper); overflow: hidden;
  }

  .masthead {
    position: absolute; left: 0; top: 0; width: 100%; height: 218px;
    display: flex; align-items: center; justify-content: center; gap: 22px;
  }
  .masthead__dot { width: 118px; height: 118px; border-radius: 50%; background: var(--brand-blue); }
  .masthead__name {
    font-family: "Montserrat", sans-serif; font-weight: 600; font-size: 76px;
    color: var(--brand-blue); letter-spacing: 1px;
  }

  .hero {
    position: absolute; left: 0; top: 218px; width: 100%; height: 458px;
    background: linear-gradient(180deg, #d98c6b 0%, #b67c79 16%, #4a5672 38%, #2c3f55 62%, #162330 100%);
  }

  .divider { position: absolute; left: 0; top: 676px; width: 100%; height: 30px; }

  .mission { position: absolute; left: 35px; top: 748px; width: 450px; }
  .mission__title {
    font-family: "Montserrat", sans-serif; font-weight: 700; font-size: 50px;
    color: var(--brand-blue); text-align: center; line-height: 1; margin-bottom: 18px;
  }
  .mission__body {
    font-family: "Arimo", Arial, sans-serif; font-size: 17.3px; line-height: 22px;
    color: var(--ink); text-align: justify; text-align-last: center; hyphens: auto;
  }

  .event {
    position: absolute; left: 520px; top: 747px; width: 600px; height: 679px;
    background: var(--brand-green); color: var(--paper); text-align: center;
    font-family: "Montserrat", sans-serif;
  }
  .event__title {
    margin-top: 60px; font-weight: 800; font-size: 57px; line-height: 71px; letter-spacing: 1px;
  }
  .event__host { margin-top: 4px; font-weight: 500; font-size: 27px; line-height: 36px; }
  .event__date { margin-top: 16px; font-weight: 800; font-size: 43px; }
  .event__badge {
    margin-top: 34px; display: flex; flex-direction: column; align-items: center; gap: 14px;
  }
  .event__badge-ring { width: 150px; height: 150px; border-radius: 50%; background: #f4f0f4; }
  .event__badge-name { font-weight: 600; font-size: 44px; }

  .contact-bar {
    position: absolute; left: 0; top: 1437px; width: 100%; height: 116px;
    background: var(--brand-blue); color: var(--paper);
    font-family: "Montserrat", sans-serif; font-weight: 500; font-size: 21px;
    display: flex; align-items: center; padding-left: 36px;
  }
  .contact-item { display: flex; align-items: center; gap: 16px; }
  .contact-item svg { flex: none; }
  .contact-item--venue { width: 455px; line-height: 27px; }
  .contact-item--phone { width: 242px; }
</style>
</head>
<body>
  <main class="flyer">
    <header class="masthead">
      <span class="masthead__dot"></span>
      <span class="masthead__name">B-AdPW</span>
    </header>

    <div class="hero" role="img" aria-label="Aerial photo of a city skyline at dusk beside a winding river"></div>

    <svg class="divider" viewBox="0 0 1120 30" preserveAspectRatio="none" aria-hidden="true">
      <rect width="1120" height="30" fill="var(--brand-green)"/>
      <polygon points="690,30 720,0 1120,0 1120,30" fill="var(--paper)"/>
      <polygon points="708,30 738,0 1120,0 1120,30" fill="var(--brand-blue)"/>
    </svg>

    <section class="mission">
      <h2 class="mission__title">OUR MISSION:</h2>
      <p class="mission__body">Architecture, Construction and Engineering are all struggling with a tremendous shortage of skilled talent. It is more important than ever for organizations to be able to attract, support and retain a talented workforce and to encourage more women to pursue and build vibrant careers in architecture, engineering and construction. Unfortunately, their attrition rate also remains high in these industries. Developing and retaining a skilled workforce includes identifying and addressing the specific needs of women in our industry. Man or Woman; Male or Female Brain, B-AdPW’s Rising Builders Summit will give you and your team the tools you need to excel as an Employer of Choice and a roadmap for individual continued career planning and success . This unique Forum provides a venue to engage everyone from executives to those just beginning their careers with active, hands-on sessions and vibrant networking with the best and brightest in the A/E/C industry. In our usual B-AdPW Forum style, Keynotes become table participants and table participants become presenters, encouraging participants to assimilate what they are learning. Join local, state and national leaders and subject matter experts as we candidly explore and address the issues affecting women in our industry</p>
    </section>

    <section class="event">
      <h1 class="event__title">5TH ANNUAL<br>RISING BUILDERS<br>SUMMIT</h1>
      <p class="event__host">by the Bureau for Advancement in<br>Public Works (B-AdPW)</p>
      <p class="event__date">JANUARY 24, 2020</p>
      <div class="event__badge">
        <span class="event__badge-ring"></span>
        <span class="event__badge-name">Rings of Merit</span>
      </div>
    </section>

    <footer class="contact-bar">
      <div class="contact-item contact-item--venue">
        <svg width="24" height="34" viewBox="0 0 24 34" aria-hidden="true">
          <path d="M12 0C5.4 0 0 5.3 0 11.9 0 20.5 12 34 12 34s12-13.5 12-22.1C24 5.3 18.6 0 12 0z" fill="var(--brand-green)"/>
          <circle cx="12" cy="12" r="4.5" fill="var(--brand-blue)"/>
        </svg>
        <span>Harborview Lodge Hotel and<br>Conference Center, San Marcos, TX</span>
      </div>
      <div class="contact-item contact-item--phone">
        <svg width="36" height="36" viewBox="0 0 36 36" aria-hidden="true">
          <circle cx="18" cy="18" r="16" fill="none" stroke="var(--brand-green)" stroke-width="2.5"/>
          <path d="M12 10c1-1 2.5-1 3 .2l1.5 3.3c.3.8 0 1.6-.6 2l-1.2.9c1 2.3 2.6 3.9 4.9 4.9l.9-1.2c.5-.6 1.3-.9 2-.6l3.3 1.5c1.2.5 1.2 2 .2 3-1.7 1.8-4.2 2.1-6.5.8-3.4-1.9-6.1-4.6-8-8-1.3-2.3-1-4.8.5-6.8z" fill="var(--brand-green)"/>
        </svg>
        <span>(512) 555-0148</span>
      </div>
      <div class="contact-item">
        <svg width="34" height="34" viewBox="0 0 34 34" aria-hidden="true" fill="none" stroke="var(--brand-green)" stroke-width="2.2">
          <circle cx="17" cy="17" r="15"/>
          <ellipse cx="17" cy="17" rx="6.5" ry="15"/>
          <line x1="2" y1="17" x2="32" y2="17"/>
          <line x1="17" y1="2" x2="17" y2="32"/>
          <path d="M5 9h24M5 25h24"/>
        </svg>
        <span>www.b-adpw.example.org</span>
      </div>
    </footer>
  </main>
</body>
</html>
```